Business Card for Start-Up Consulting Business
TK Advisory Partners, LLC
Business Card for Start-Up Consulting Business - Consulting
Creative Brief
Professional
Roderick Lyle Pemberton
President/CEO
82 Fenwhistle Court #2410 Dover, DE 19906
info@tkapllc.example
www.tkapllc.example
On the back of the card, I would like something like: Text TKTEAM to 38217 for updates and promotions or For updates and promotions, text TKTEAM to 38217. I would also like to have our services listed on the back of the card like: We Specialize In: or Our Services Includes: *Negative Equity Financing *Tax Mitigation *Life & Health Insurance *Merchant Processing *Telecommunications *Energy Saving Programs *Marketing & Advertising and *More. And if the back is not crowded, maybe we can added the phone, fax, email and/or web address. Thanks

```html
<!DOCTYPE html>
<html lang="en">
<head>
<meta charset="utf-8">
<title>TK Advisory Partners, LLC – Business Card</title>
<link href="https://fonts.googleapis.com/css2?family=Tinos:ital,wght@0,400;0,700;1,400;1,700&display=swap" rel="stylesheet">
<style>
  :root {
    --navy: #1d3f8a;
    --navy-dark: #142f6b;
    --green: #6db52e;
    --ink: #2a2a2a;
    --rule: #bbbbbb;
    --paper: #ffffff;
    --backdrop: #e6e8ec;
  }
  * { box-sizing: border-box; margin: 0; padding: 0; }
  html, body { width: 1200px; height: 901px; overflow: hidden; }
  body {
    background: var(--backdrop);
    font-family: "Tinos", "Times New Roman", serif;
    color: var(--ink);
    position: relative;
  }
  .card {
    position: absolute;
    left: 240px;
    width: 720px;
    height: 411px;
    background: var(--paper);
    border-radius: 22px;
    overflow: hidden;
    box-shadow: 0 6px 20px rgba(0,0,0,.15);
  }
  .card--back { top: 26px; }
  .card--front { top: 464px; }

  /* back */
  .services { position: absolute; left: 44px; top: 56px; }
  .services__title {
    font-style: italic; font-weight: 700; color: var(--navy);
    font-size: 20px; text-decoration: underline; margin-bottom: 18px;
  }
  .services__list { list-style: none; }
  .services__item {
    font-size: 19px; color: var(--ink); margin-bottom: 17px;
    display: flex; align-items: center; gap: 14px;
  }
  .services__item::before {
    content: ""; width: 10px; height: 10px; border-radius: 50%;
    background: var(--navy); flex: none;
  }
  .services__item:nth-child(odd)::before { background: var(--green); }

  .back-brand {
    position: absolute; left: 420px; top: 96px; width: 260px;
    display: flex; align-items: center; gap: 12px;
  }
  .brand-square { width: 34px; height: 34px; background: var(--navy); flex: none; }
  .back-brand .brand-name { font-size: 22px; font-weight: 700; color: var(--navy); line-height: 1.1; }
  .text-offer {
    position: absolute; left: 420px; top: 210px; width: 260px;
    font-size: 19px; line-height: 1.25; color: var(--ink);
  }

  /* front */
  .front-brand { position: absolute; left: 40px; top: 34px; }
  .front-brand__row { display: flex; align-items: center; gap: 12px; }
  .front-brand .brand-name { font-size: 28px; font-weight: 700; color: var(--navy); }
  .tagline {
    margin: 6px 0 0 46px; font-size: 11px; letter-spacing: 1.5px;
    color: var(--green); font-weight: 700; font-style: italic;
  }
  .bands { position: absolute; left: 0; top: 186px; width: 720px; height: 70px; }
  .person { position: absolute; right: 40px; top: 150px; text-align: right; }
  .person__name { font-size: 21px; font-weight: 700; color: var(--navy); }
  .person__role { font-size: 17px; color: var(--ink); }
  .website {
    position: absolute; right: 40px; top: 222px;
    color: var(--paper); font-size: 17px; letter-spacing: 2px;
  }
  .contact { position: absolute; top: 286px; font-size: 17px; line-height: 1.4; white-space: nowrap; }
  .contact--address { left: 40px; }
  .contact--phones, .contact--office {
    display: grid; grid-template-columns: 18px auto; column-gap: 12px; align-items: center;
    padding-left: 20px; border-left: 1px solid var(--rule);
  }
  .contact--phones { left: 290px; }
  .contact--office { left: 462px; }
  .icon { width: 17px; height: 17px; fill: var(--ink); }
</style>
</head>
<body>

<section class="card card--back" aria-label="Card back">
  <div class="services">
    <h2 class="services__title">Our Services Includes:</h2>
    <ul class="services__list">
      <li class="services__item">Negative Equity Financing</li>
      <li class="services__item">Tax Mitigation</li>
      <li class="services__item">Life &amp; Health Insurance</li>
      <li class="services__item">Merchant Processing</li>
      <li class="services__item">Telecommunications</li>
      <li class="services__item">Energy Saving Programs</li>
      <li class="services__item">Marketing &amp; Advertising</li>
    </ul>
  </div>
  <div class="back-brand">
    <span class="brand-square"></span>
    <span class="brand-name">TK Advisory Partners, LLC</span>
  </div>
  <p class="text-offer">Text TKTEAM to 38217<br>for updates and promotions</p>
</section>

<section class="card card--front" aria-label="Card front">
  <div class="front-brand">
    <div class="front-brand__row">
      <span class="brand-square"></span>
      <span class="brand-name">TK Advisory Partners, LLC</span>
    </div>
    <p class="tagline">HELPING BUSINESSES SAVE MONEY!</p>
  </div>

  <svg class="bands" viewBox="0 0 720 70" aria-hidden="true">
    <polygon points="0,20 260,20 270,40 0,40" fill="var(--green)"/>
    <polygon points="250,20 720,20 720,58 290,58" fill="var(--navy)"/>
    <polygon points="250,20 268,20 300,58 290,58" fill="var(--navy-dark)"/>
  </svg>

  <div class="person">
    <p class="person__name">Roderick Lyle Pemberton</p>
    <p class="person__role">President/CEO</p>
  </div>
  <p class="website">www.tkapllc.example</p>

  <p class="contact contact--address">82 Fenwhistle Court #2410<br>Dover, DE 19906</p>

  <div class="contact contact--phones">
    <svg class="icon" viewBox="0 0 24 24" aria-label="Phone"><path d="M6.6 10.8a15 15 0 0 0 6.6 6.6l2.2-2.2c.3-.3.7-.4 1-.2 1.1.4 2.3.6 3.6.6.6 0 1 .4 1 1V20c0 .6-.4 1-1 1A17 17 0 0 1 3 4c0-.6.4-1 1-1h3.5c.6 0 1 .4 1 1 0 1.3.2 2.5.6 3.6.1.3 0 .7-.2 1z"/></svg>
    <span>(302) 555-0148</span>
    <svg class="icon" viewBox="0 0 24 24" aria-label="Mobile"><path d="M7 1h10a2 2 0 0 1 2 2v18a2 2 0 0 1-2 2H7a2 2 0 0 1-2-2V3a2 2 0 0 1 2-2zm0 3v14h10V4zm5 15.5a1 1 0 1 0 0 2 1 1 0 0 0 0-2z"/></svg>
    <span>(302) 555-0193</span>
  </div>

  <div class="contact contact--office">
    <svg class="icon" viewBox="0 0 24 24" aria-label="Fax"><path d="M6 2h10l2 2v5H6zM3 10h18a1 1 0 0 1 1 1v8a1 1 0 0 1-1 1h-3v2H6v-2H3a1 1 0 0 1-1-1v-8a1 1 0 0 1 1-1zm5 7v3h8v-3z"/></svg>
    <span>(888) 555-0162</span>
    <svg class="icon" viewBox="0 0 24 24" aria-label="Email"><path d="M2 5h20v14H2zm2 2v.5l8 5 8-5V7zm0 2.8V17h16V9.8l-8 5z"/></svg>
    <span>info@tkapllc.example</span>
  </div>
</section>

</body>
</html>
```